IRON SASH VIGOUR CERTIFICATE

Carrowby Hapkido Inc is wanting to introduce a fitness system based upon certificates reflecting rank; White - Yellow - Blue - Red - Black.

The Certificate "MUST" have on it "IRON SASH VIGOUR"

The Certificate "MUST" have a martial arts theme!

The Certificate "MUST" reflect the fitness requirements for each rank.

The colour scheme for each Certificate "MUST" reflect the belt rank

The Certificate must include at least one martial arts graphic / motif

The certificate must have the Carrowby HKD LOGO

We will need a certificate template that can be for all levels but reflect the rank and fitness level. The certificate can be either traditional or modern style but must reflect a martial art themes. The certificate must have the Carrowby Hapkido logo incorporated into the certificate with signature space for senior instructors Dan Pellow & Sorna Vick-Pellow. The certificates should be eye catching and exciting to look at. It should bold and incorporate martial art motifs etc The fitness requirements are not onerous and the certificate system is created to incentivise physical activity and correct technique rather than creating an impossible standards only Olympians can achieve. The majority of our students are upper primary and lower secondary from 11yr-15yrs. Certificate should be youthful but not silly. The certificate template will be reproduced for each colour belt.White = 10 push ups 10 Sit ups 10 squats 10 Jumping Jacks 20 sec plank 400m continuous run Demonstrate beginner stretching techniqueYellow = 20 push ups 20 sit ups 20 squats 20 Jumping Jacks 40 Sec plank 800m continuous run Demonstrate intermediate stretching techniqueBlue = 30 push ups 30 sit ups 30 squats 30 Jumping Jacks 60 Sec plank 1200m continuous run Demonstrate intermediate stretching techniqueRed = 40 push ups 40 sit ups 40 squats 40 Jumping Jacks 75sec plank 1600m run Demonstrate advanced stretching techniqueBlack = 50 push ups 50 sit ups 50 squats 50 Jumping jacks 90 sec planks 2000m continuous run Demonstrate advanced stretching technique
Updates

HI Designers, Please go for modern and professionals. Several designs have used traditional motifs of water dragons or lattice bordering. This looks old school. Please do not use martial art silhouettes as it looks amateur. Definately looking for upmarket high quality presentations.

Logo Text

IRON SASH VIGOUR

Font styles to use
Decorative

Colors

Designer to choose colors to be used in the design.

Requirements
Must have
• This will be a template foe all coloured ranks of fitness, Be bold, memorable, should be themed to martial arts etc

```html
<!DOCTYPE html>
<html lang="en">
<head>
<meta charset="utf-8">
<title>Iron Sash Vigour Certificates</title>
<link rel="stylesheet" href="https://fonts.googleapis.com/css2?family=Montserrat:wght@400;500;700;800&family=Cinzel:wght@400&display=swap">
<style>
  :root {
    --navy: #262b3a;
    --ink: #141414;
    --paper: #ffffff;
    --paper-shade: #eceef1;
    --red: #e3161f;
    --yellow: #e8b21c;
    --blue: #1530e0;
    --black: #15171d;
    --white-belt: #d3d6dc;
  }
  * { box-sizing: border-box; margin: 0; padding: 0; }
  html, body { width: 794px; height: 1200px; overflow: hidden; background: var(--paper); }
  body { position: relative; font-family: "Montserrat", Arial, sans-serif; color: var(--ink); }

  .slot { position: absolute; }
  .slot-main { left: 43px; top: 42px; }
  .slot-small { width: 334px; height: 258px; }
  .slot-small .certificate { transform: scale(0.48); transform-origin: 0 0; }
  .slot-black { left: 43px; top: 606px; }
  .slot-yellow { left: 407px; top: 611px; }
  .slot-white { left: 43px; top: 894px; }
  .slot-blue { left: 407px; top: 894px; }

  .certificate {
    position: relative; width: 696px; height: 538px; overflow: hidden;
    background: linear-gradient(135deg, var(--paper) 0%, var(--paper-shade) 50%, var(--paper) 100%);
    box-shadow: 0 4px 14px rgba(0,0,0,.35);
  }
  .certificate.small-shadow { box-shadow: 0 8px 24px rgba(0,0,0,.45); }
  .rank-red { --accent: var(--red); --rank-text: var(--red); }
  .rank-black { --accent: var(--black); --rank-text: var(--black); }
  .rank-yellow { --accent: var(--yellow); --rank-text: var(--yellow); }
  .rank-white { --accent: var(--white-belt); --rank-text: var(--black); }
  .rank-blue { --accent: var(--blue); --rank-text: var(--blue); }

  .frame { position: absolute; inset: 0; width: 100%; height: 100%; }
  .frame .dark { fill: var(--navy); }
  .frame .accent { fill: var(--accent); }

  .club-mark {
    position: absolute; right: 30px; top: 56px; width: 150px;
    display: flex; align-items: center; gap: 8px;
  }
  .club-mark .dot { width: 18px; height: 18px; border-radius: 50%; background: var(--navy); flex: none; }
  .club-mark .club-name {
    font-weight: 800; font-size: 17px; line-height: 1.1; color: var(--navy); text-transform: uppercase;
  }

  .title { position: absolute; left: 0; right: 0; top: 96px; text-align: center; line-height: 1; }
  .title .title-main { display: block; font-weight: 800; font-size: 44px; letter-spacing: -1px; }
  .title .title-sub { display: block; font-weight: 400; font-size: 18px; margin-top: 1px; }

  .recipient {
    position: absolute; left: 82px; width: 534px; top: 186px; padding-bottom: 8px;
    border-bottom: 1.5px solid var(--ink);
    text-align: center; font-family: "Cinzel", Georgia, serif; font-size: 50px; line-height: 1.1;
  }
  .statement { position: absolute; left: 0; right: 0; top: 262px; text-align: center; }
  .statement .lead { font-size: 12.5px; }
  .statement .rank { font-weight: 800; font-size: 46px; letter-spacing: -1px; line-height: 1.05; color: var(--rank-text); }
  .statement .requirements { font-size: 11px; line-height: 1.3; width: 440px; margin: 0 auto; }
  .statement .awarded { font-size: 13px; margin-top: 12px; }

  .signature { position: absolute; top: 426px; width: 205px; border-top: 1.5px solid var(--ink); text-align: center; padding-top: 10px; }
  .signature-left { left: 82px; }
  .signature-right { left: 410px; }
  .signature .signer { font-weight: 700; font-size: 14px; text-transform: uppercase; white-space: nowrap; }
  .signature .role { font-size: 13px; }

  .motif {
    position: absolute; left: 300px; top: 390px; width: 96px; height: 120px; border-radius: 8px;
    background: radial-gradient(ellipse at 50% 50%, var(--accent) 0%, rgba(38,43,58,.25) 70%, transparent 100%);
  }
</style>
</head>
<body>

<div class="slot slot-main">
  <article class="certificate rank-red">
    <svg class="frame" viewBox="0 0 696 538" aria-hidden="true">
      <polygon class="dark" points="0,0 430,0 140,110 60,160 0,300"/>
      <polygon class="accent" points="100,126 140,110 430,0 470,0 150,118"/>
      <polygon class="accent" points="52,168 72,160 18,318 0,330 0,300"/>
      <polygon class="dark" points="696,300 696,538 430,538 630,470 662,418"/>
      <polygon class="accent" points="696,240 696,290 660,410 650,404"/>
      <polygon class="accent" points="470,538 640,476 650,484 520,538"/>
    </svg>
    <div class="club-mark"><span class="dot"></span><span class="club-name">Carrowby Hapkido</span></div>
    <h1 class="title"><span class="title-main">IRON SASH</span><span class="title-sub">VIGOUR</span></h1>
    <p class="recipient">Name Lastname</p>
    <div class="statement">
      <p class="lead">is certificated to hold the rank of</p>
      <p class="rank">RED BELT</p>
      <p class="requirements">40 push ups, 40 sit ups, 40 squats, 40 Jumping Jacks, 75sec plank, 1600m run, Demonstrate advanced stretching technique</p>
      <p class="awarded">Awarded on 29th November 2018 at Carrowby Hapkido Gymnasium.</p>
    </div>
    <div class="signature signature-left"><p class="signer">Dan Pellow</p><p class="role">Senior Instructor</p></div>
    <div class="motif" role="img" aria-label="Flaming kick motif in belt colour"></div>
    <div class="signature signature-right"><p class="signer">Sorna Vick-Pellow</p><p class="role">Senior Instructor</p></div>
  </article>
</div>

<div class="slot slot-small slot-black">
  <article class="certificate small-shadow rank-black">
    <svg class="frame" viewBox="0 0 696 538" aria-hidden="true">
      <polygon class="dark" points="0,0 430,0 140,110 60,160 0,300"/>
      <polygon class="accent" points="100,126 140,110 430,0 470,0 150,118"/>
      <polygon class="accent" points="52,168 72,160 18,318 0,330 0,300"/>
      <polygon class="dark" points="696,300 696,538 430,538 630,470 662,418"/>
      <polygon class="accent" points="696,240 696,290 660,410 650,404"/>
      <polygon class="accent" points="470,538 640,476 650,484 520,538"/>
    </svg>
    <div class="club-mark"><span class="dot"></span><span class="club-name">Carrowby Hapkido</span></div>
    <h2 class="title"><span class="title-main">IRON SASH</span><span class="title-sub">VIGOUR</span></h2>
    <p class="recipient">Name Lastname</p>
    <div class="statement">
      <p class="lead">is certificated to hold the rank of</p>
      <p class="rank">BLACK BELT</p>
      <p class="requirements">50 push ups, 50 sit ups, 50 squats, 50 Jumping jacks, 90 sec planks, 2000m continuous run, Demonstrate advanced stretching technique</p>
      <p class="awarded">Awarded on 29th November 2018 at Carrowby Hapkido Gymnasium.</p>
    </div>
    <div class="signature signature-left"><p class="signer">Dan Pellow</p><p class="role">Senior Instructor</p></div>
    <div class="motif" role="img" aria-label="Flaming kick motif in belt colour"></div>
    <div class="signature signature-right"><p class="signer">Sorna Vick-Pellow</p><p class="role">Senior Instructor</p></div>
  </article>
</div>

<div class="slot slot-small slot-yellow">
  <article class="certificate small-shadow rank-yellow">
    <svg class="frame" viewBox="0 0 696 538" aria-hidden="true">
      <polygon class="dark" points="0,0 430,0 140,110 60,160 0,300"/>
      <polygon class="accent" points="100,126 140,110 430,0 470,0 150,118"/>
      <polygon class="accent" points="52,168 72,160 18,318 0,330 0,300"/>
      <polygon class="dark" points="696,300 696,538 430,538 630,470 662,418"/>
      <polygon class="accent" points="696,240 696,290 660,410 650,404"/>
      <polygon class="accent" points="470,538 640,476 650,484 520,538"/>
    </svg>
    <div class="club-mark"><span class="dot"></span><span class="club-name">Carrowby Hapkido</span></div>
    <h2 class="title"><span class="title-main">IRON SASH</span><span class="title-sub">VIGOUR</span></h2>
    <p class="recipient">Name Lastname</p>
    <div class="statement">
      <p class="lead">is certificated to hold the rank of</p>
      <p class="rank">YELLOW BELT</p>
      <p class="requirements">20 push ups, 20 sit ups, 20 squats, 20 Jumping Jacks, 40 Sec plank, 800m continuous run, Demonstrate intermediate stretching technique</p>
      <p class="awarded">Awarded on 29th November 2018 at Carrowby Hapkido Gymnasium.</p>
    </div>
    <div class="signature signature-left"><p class="signer">Dan Pellow</p><p class="role">Senior Instructor</p></div>
    <div class="motif" role="img" aria-label="Flaming kick motif in belt colour"></div>
    <div class="signature signature-right"><p class="signer">Sorna Vick-Pellow</p><p class="role">Senior Instructor</p></div>
  </article>
</div>

<div class="slot slot-small slot-white">
  <article class="certificate small-shadow rank-white">
    <svg class="frame" viewBox="0 0 696 538" aria-hidden="true">
      <polygon class="dark" points="0,0 430,0 140,110 60,160 0,300"/>
      <polygon class="accent" points="100,126 140,110 430,0 470,0 150,118"/>
      <polygon class="accent" points="52,168 72,160 18,318 0,330 0,300"/>
      <polygon class="dark" points="696,300 696,538 430,538 630,470 662,418"/>
      <polygon class="accent" points="696,240 696,290 660,410 650,404"/>
      <polygon class="accent" points="470,538 640,476 650,484 520,538"/>
    </svg>
    <div class="club-mark"><span class="dot"></span><span class="club-name">Carrowby Hapkido</span></div>
    <h2 class="title"><span class="title-main">IRON SASH</span><span class="title-sub">VIGOUR</span></h2>
    <p class="recipient">Name Lastname</p>
    <div class="statement">
      <p class="lead">is certificated to hold the rank of</p>
      <p class="rank">WHITE BELT</p>
      <p class="requirements">10 push ups, 10 Sit ups, 10 squats, 10 Jumping Jacks, 20 sec plank, 400m continuous run, Demonstrate beginner stretching technique</p>
      <p class="awarded">Awarded on 29th November 2018 at Carrowby Hapkido Gymnasium.</p>
    </div>
    <div class="signature signature-left"><p class="signer">Dan Pellow</p><p class="role">Senior Instructor</p></div>
    <div class="motif" role="img" aria-label="Flaming kick motif in belt colour"></div>
    <div class="signature signature-right"><p class="signer">Sorna Vick-Pellow</p><p class="role">Senior Instructor</p></div>
  </article>
</div>

<div class="slot slot-small slot-blue">
  <article class="certificate small-shadow rank-blue">
    <svg class="frame" viewBox="0 0 696 538" aria-hidden="true">
      <polygon class="dark" points="0,0 430,0 140,110 60,160 0,300"/>
      <polygon class="accent" points="100,126 140,110 430,0 470,0 150,118"/>
      <polygon class="accent" points="52,168 72,160 18,318 0,330 0,300"/>
      <polygon class="dark" points="696,300 696,538 430,538 630,470 662,418"/>
      <polygon class="accent" points="696,240 696,290 660,410 650,404"/>
      <polygon class="accent" points="470,538 640,476 650,484 520,538"/>
    </svg>
    <div class="club-mark"><span class="dot"></span><span class="club-name">Carrowby Hapkido</span></div>
    <h2 class="title"><span class="title-main">IRON SASH</span><span class="title-sub">VIGOUR</span></h2>
    <p class="recipient">Name Lastname</p>
    <div class="statement">
      <p class="lead">is certificated to hold the rank of</p>
      <p class="rank">BLUE BELT</p>
      <p class="requirements">30 push ups, 30 sit ups, 30 squats, 30 Jumping Jacks, 60 Sec plank, 1200m continuous run, Demonstrate intermediate stretching technique</p>
      <p class="awarded">Awarded on 29th November 2018 at Carrowby Hapkido Gymnasium.</p>
    </div>
    <div class="signature signature-left"><p class="signer">Dan Pellow</p><p class="role">Senior Instructor</p></div>
    <div class="motif" role="img" aria-label="Flaming kick motif in belt colour"></div>
    <div class="signature signature-right"><p class="signer">Sorna Vick-Pellow</p><p class="role">Senior Instructor</p></div>
  </article>
</div>

</body>
</html>
```